Elderwell Solutions company needs a homepage design

We need a homepage designed for a new company based in Des Moines, IA called Go Elderwell Solutions. They sell Elderwell Supplement plans to seniors. The design should communicate trust, security, be vibrant and easy to read with larger font and clear messages. The goal for visitors is to ultimately get a free quote and purchase a plan after a call from a licensed agent.

Industry/Entity Type

It Company

```html
<!DOCTYPE html>
<html lang="en">
<head>
<meta charset="utf-8">
<title>Go Elderwell Solutions – Homepage</title>
<link href="https://fonts.googleapis.com/css2?family=Open+Sans:wght@300;400;600;700&display=swap" rel="stylesheet">
<style>
:root{
  --teal:#1a8fb8;
  --blue:#1b9fd0;
  --blue-light:#32b4e0;
  --orange:#f47b1f;
  --orange-dark:#e0660e;
  --lime:#8dc21f;
  --ink:#333a40;
  --muted:#7a8288;
  --line:#d9dde0;
  --paper:#ffffff;
  --mist:#f1f2f3;
  --footer:#a8a9aa;
}
*{box-sizing:border-box;margin:0;padding:0}
html,body{width:1200px;height:3416px;overflow:hidden;background:var(--paper)}
body{font-family:"Open Sans",Arial,sans-serif;color:var(--ink)}
.page{position:relative;width:1200px;height:3416px;overflow:hidden}
.abs{position:absolute}

/* header */
.site-header{position:absolute;left:0;top:0;width:1200px;height:105px;background:var(--paper);z-index:2}
.brand{position:absolute;left:114px;top:32px;font-size:29px;font-weight:600;color:var(--teal)}
.topbar{position:absolute;right:110px;top:16px;display:flex;gap:26px;font-size:15px;color:var(--ink);align-items:center}
.topbar span{display:flex;align-items:center;gap:7px}
.topbar svg{width:16px;height:16px;fill:var(--teal)}
.topbar .phone{font-size:17px;font-weight:600}
.main-nav{position:absolute;left:517px;top:60px;display:flex;gap:34px;font-size:16px;color:var(--muted)}
.btn-consult{position:absolute;left:886px;top:57px;width:182px;height:34px;border:2px solid var(--orange);color:var(--orange);font-size:15px;display:flex;align-items:center;justify-content:center}

/* hero */
.hero{position:absolute;left:0;top:105px;width:1200px;height:533px}
.hero-photo{position:absolute;inset:0;background:linear-gradient(100deg,#c9a57e 0%,#e8d2bb 22%,#b9c9a0 45%,#e9efe0 60%,#f7f9f4 100%)}
.hero-copy{position:absolute;left:633px;top:146px;width:470px}
.hero-copy h1{font-size:34px;line-height:42px;font-weight:600;color:var(--teal);text-transform:uppercase;letter-spacing:.5px}
.hero-copy p{margin-top:14px;font-size:17px;line-height:23px;color:var(--teal)}
.btn{display:inline-flex;align-items:center;justify-content:center;color:#fff;font-size:16px;font-weight:600}
.btn-orange{background:linear-gradient(var(--orange),var(--orange-dark))}
.btn-blue{background:linear-gradient(var(--blue-light),var(--blue))}
.hero-copy .btn{margin-top:22px;width:218px;height:46px}

/* features */
.features{position:absolute;left:0;top:638px;width:1200px;height:352px;background:var(--blue)}
.feature{position:absolute;top:0;width:348px;height:290px;text-align:center;color:#fff;padding-top:56px}
.feature.highlight{background:var(--blue-light)}
.feature svg{width:60px;height:60px;stroke:#fff;fill:none;stroke-width:2.4}
.feature h3{font-size:26px;font-weight:400;margin-top:12px}
.feature p{font-size:13px;line-height:19px;margin:8px auto 0;width:250px}
.wave{position:absolute;left:0;top:225px}

/* welcome */
.welcome{position:absolute;left:0;top:900px;width:1200px;height:512px;background:linear-gradient(90deg,#f3f3f2,#fbfbfa 60%)}
.welcome-photo{position:absolute;left:604px;top:30px;width:596px;height:482px;background:linear-gradient(135deg,#e6e2dc,#b9978a 45%,#d8c6bd 70%,#cfcfd1)}
.welcome-copy{position:absolute;left:118px;top:135px;width:480px}
.welcome-copy .pre{font-size:35px;font-weight:300;color:#9aa0a4;line-height:42px}
.welcome-copy h2{font-size:37px;font-weight:400;line-height:44px;color:var(--ink)}
.welcome-copy p{margin-top:18px;font-size:15px;line-height:24px;color:var(--muted)}
.welcome-copy .btn{margin-top:28px;width:156px;height:45px}

/* plans table */
.plans{position:absolute;left:0;top:1412px;width:1200px;height:535px;background:var(--mist)}
.section-title{text-align:center;font-size:30px;font-weight:400;color:var(--ink)}
.plans .section-title{position:absolute;top:36px;width:100%;display:flex;justify-content:center;align-items:center;gap:16px}
.plans .section-title::before,.plans .section-title::after{content:"";width:40px;height:1px;background:#888}
.plan-table{position:absolute;left:114px;top:107px;width:970px;border-collapse:collapse;background:#fff;font-size:11.5px;table-layout:fixed}
.plan-table th{height:48px;background:var(--blue-light);color:#fff;font-weight:400;font-size:17px;border-right:1px solid #6cc8e8}
.plan-table th.benefits{background:var(--lime);text-align:left;padding-left:30px;width:239px;font-size:17px;border-right:none}
.plan-table td{border:1px solid var(--line);text-align:center;color:var(--ink)}
.plan-table td.label{background:var(--lime);color:#fff;text-align:left;padding-left:26px;border:none;border-bottom:1px solid #a7d450;font-size:12.5px;line-height:17px}

/* why choose */
.why{position:absolute;left:0;top:1947px;width:1200px;height:467px;background:linear-gradient(90deg,#f4f6f8,#fbfcfd)}
.why-photo{position:absolute;left:0;top:10px;width:604px;height:457px;background:linear-gradient(110deg,#e3dcd6,#c9b3b7 40%,#eef0f2 65%,#dde7ee)}
.why-copy{position:absolute;left:620px;top:100px;width:470px}
.why-copy h2{font-size:32px;font-weight:400;color:var(--teal)}
.why-copy p{margin-top:18px;font-size:15px;line-height:24px;color:var(--muted)}
.why-copy .btn{margin-top:26px;width:148px;height:41px}

/* testimonials */
.clients{position:absolute;left:0;top:2414px;width:1200px;height:422px;background:#fff}
.clients .section-title{position:absolute;top:46px;width:100%;font-size:32px}
.quote-card{position:absolute;top:144px;width:430px;height:219px;border:2px solid var(--line);text-align:center;padding:58px 46px 0}
.avatar{position:absolute;left:163px;top:-52px;width:104px;height:104px;border-radius:50%;border:3px solid var(--line)}
.quote-card blockquote{font-size:14px;font-style:italic;line-height:22px;color:var(--muted);position:relative}
.quote-card blockquote::before{content:"\201C";position:absolute;left:-6px;top:-14px;font-size:40px;color:var(--blue-light);font-style:normal}
.quote-card blockquote::after{content:"\201D";position:absolute;right:8px;bottom:-40px;font-size:40px;color:var(--blue-light);font-style:normal}
.quote-card cite{display:block;margin-top:14px;font-style:normal;font-size:15px;color:var(--ink)}

/* footer */
.site-footer{position:absolute;left:0;top:2836px;width:1200px;height:580px;background:var(--footer);color:#fff}
.footer-brand{position:absolute;left:148px;top:74px;font-size:35px;line-height:38px;font-weight:400;color:#eeeeee}
.footer-col{position:absolute;top:84px}
.footer-col h4{font-size:19px;font-weight:400;letter-spacing:.5px;margin-bottom:8px}
.footer-col li{list-style:none;font-size:14px;line-height:31px;color:#f4f4f4}
.social{display:flex;gap:8px;margin-top:10px}
.social i{display:block;width:30px;height:30px;border:2px solid #fff;border-radius:50%}
.disclaimer{position:absolute;left:130px;top:346px;width:940px;font-size:11.5px;line-height:17px;color:#f2f2f2}
.disclaimer p{margin-bottom:6px}
.footer-rule{position:absolute;left:130px;top:512px;width:940px;height:1px;background:#c4c4c4}
.copyright{position:absolute;top:534px;width:100%;text-align:center;font-size:12px;color:#f2f2f2}
</style>
</head>
<body>
<div class="page">

<header class="site-header">
  <div class="brand">Go Elderwell Solutions</div>
  <div class="topbar">
    <span><svg viewBox="0 0 16 16"><path d="M1 3h14v10H1z M1 3l7 6 7-6" fill="var(--teal)"/><path d="M1.5 3.5l6.5 5.5 6.5-5.5" stroke="#fff" stroke-width="1.4" fill="none"/></svg>info@elderwell.com</span>
    <span><svg viewBox="0 0 16 16"><circle cx="8" cy="8" r="6.5" fill="none" stroke="var(--teal)" stroke-width="1.8"/><path d="M8 4v4.5h3" stroke="var(--teal)" stroke-width="1.8" fill="none"/></svg>Hours 8-6CST</span>
    <span class="phone"><svg viewBox="0 0 16 16"><path d="M3 1.5l3 .5 1 3.5-2 1.5c1 2 2.5 3.5 4.5 4.5l1.5-2 3.5 1 .5 3c-1 1-2 1.5-3 1.5C6 15 1 10 1 4.5c0-1 .5-2 2-3z"/></svg>555.010.2848</span>
  </div>
  <nav class="main-nav"><span>Plans</span><span>Resources</span><span>About Us</span><span>Contact</span></nav>
  <div class="btn-consult">Free Consultation</div>
</header>

<section class="hero">
  <div class="hero-photo" role="img" aria-label="Photo of a smiling senior couple embracing outdoors in a sunny park"></div>
  <div class="hero-copy">
    <h1>Selecting an Elderwell plan is an unexpectedly daunting task</h1>
    <p>Our trusted advisors are here to educate, inform, and guide you through this process</p>
    <span class="btn btn-orange">Get a Free Quote</span>
  </div>
</section>

<section class="welcome">
  <div class="welcome-photo" role="img" aria-label="Photo of a smiling woman with glasses and a pearl necklace"></div>
  <div class="welcome-copy">
    <div class="pre">Welcome to</div>
    <h2>Elderwell Solutions</h2>
    <p>Ateger congue augue et malesuada iaculis ipsum dui aliquet felis at cursus magna nisl nec elit Praesent elementum elit at tellus nec ultricies sit amet porttitor mattis enim<br>In massa libero lointerdum nec interdum vel blandit sed nulla in ullamcorper est eget tempor cursus mi consect</p>
    <span class="btn btn-orange">Learn More</span>
  </div>
</section>

<section class="features">
  <div class="feature" style="left:78px">
    <svg viewBox="0 0 60 60"><path d="M30 5l21 8v15c0 13-9 22-21 27C18 50 9 41 9 28V13z"/><path d="M21 30l7 7 12-14"/></svg>
    <h3>Security</h3>
    <p>Class aptent taciti sociosqu ad litora torquent per conubia nostra per inceptos hymenaeos Proin nulla arcu</p>
  </div>
  <div class="feature highlight" style="left:426px">
    <svg viewBox="0 0 60 60"><circle cx="30" cy="30" r="26"/><circle cx="30" cy="30" r="18"/><path d="M22 30l6 6 11-12"/></svg>
    <h3>100% Trust</h3>
    <p>Class aptent taciti sociosqu ad litora torquent per conubia nostra per inceptos hymenaeos Proin nulla arcu</p>
  </div>
  <div class="feature" style="left:774px">
    <svg viewBox="0 0 60 60"><path d="M30 52C14 40 5 31 5 20 5 12 11 7 18 7c5 0 9 3 12 7 3-4 7-7 12-7 7 0 13 5 13 13 0 11-9 20-25 32z"/><path d="M8 30h13l4-8 6 15 5-10h16"/></svg>
    <h3>Experienced</h3>
    <p>Class aptent taciti sociosqu ad litora torquent per conubia nostra per inceptos hymenaeos Proin nulla arcu</p>
  </div>
  <svg class="wave" width="1200" height="127" viewBox="0 0 1200 127">
    <path d="M0 120 C300 40 800 20 1200 50 L1200 127 L0 127z" fill="#f4f4f3"/>
    <path d="M0 110 C300 30 800 10 1200 40" stroke="#ffffff" stroke-width="6" fill="none"/>
  </svg>
</section>

<section class="plans">
  <h2 class="section-title">Supplement Plans</h2>
  <table class="plan-table">
    <thead>
      <tr><th class="benefits">BENEFITS</th><th>A</th><th>B</th><th>C</th><th>D</th><th>E</th><th>F</th><th>G</th><th>H</th><th>I</th><th>J</th><th>K</th><th>L</th><th>M</th><th>N</th></tr>
    </thead>
    <tbody>
      <tr style="height:68px"><td class="label">Interdum vel blandit<br>Sed nulla in ullamcorpeget</td><td>100%</td><td>100%</td><td>100%</td><td>100%</td><td>100%</td><td>100%</td><td>100%</td><td>100%</td><td>100%</td><td>100%</td><td>100%</td><td>100%</td><td>100%</td><td>100%</td></tr>
      <tr style="height:34px"><td class="label">tempor cursus neq</td><td>100%</td><td>100%</td><td>100%</td><td>100%</td><td>100%</td><td>100%</td><td>50%</td><td>600%</td><td>100%</td><td>100%</td><td>40%</td><td></td><td>100%</td><td>80%</td></tr>
      <tr style="height:39px"><td class="label">Ai consectetuer mi a ultricies</td><td>100%</td><td>100%</td><td>100%</td><td>100%</td><td>100%</td><td>100%</td><td></td><td>100%</td><td>100%</td><td>100%</td><td>100%</td><td></td><td></td><td>100%</td></tr>
      <tr style="height:34px"><td class="label">massa est sed nisl Class</td><td>100%</td><td>100%</td><td>70%</td><td>100%</td><td></td><td></td><td></td><td></td><td></td><td>100%</td><td></td><td></td><td>100%</td><td></td></tr>
      <tr style="height:36px"><td class="label">Pptent taciti sociosqu</td><td>100%</td><td>100%</td><td>100%</td><td>100%</td><td>100%</td><td>100%</td><td></td><td>100%</td><td>100%</td><td>100%</td><td>100%</td><td>100%</td><td>100%</td><td>100%</td></tr>
      <tr style="height:36px"><td class="label">Bd litora torquent per</td><td></td><td>100%</td><td></td><td></td><td>100%</td><td>100%</td><td>50%</td><td>100%</td><td>100%</td><td></td><td>100%</td><td>100%</td><td></td><td>100%</td></tr>
      <tr style="height:34px"><td class="label">cnostra per inceptos</td><td></td><td></td><td>80%</td><td></td><td>80%</td><td></td><td>100%</td><td></td><td>70%</td><td></td><td></td><td></td><td></td><td></td></tr>
      <tr style="height:64px"><td class="label">Gymenaeos Proin</td><td></td><td></td><td>80%</td><td></td><td>80%</td><td></td><td>100%</td><td></td><td></td><td></td><td></td><td></td><td></td><td>40%</td></tr>
    </tbody>
  </table>
</section>

<section class="why">
  <div class="why-photo" role="img" aria-label="Photo of a nurse with a stethoscope comforting a smiling senior woman"></div>
  <div class="why-copy">
    <h2>Why Choose Our Plans</h2>
    <p>Donec dictum lectus non odio Cras a ante vitae enim iaculis aliquam Mauris nunc quam venenatis</p>
    <p>Donec dictum lectus non odio Cras a ante vitae enim iaculis aliquam Mauris nunc quam venenatis nec euismod sit amet egestas placerat est Pellentesque habitant</p>
    <span class="btn btn-blue">Learn More</span>
  </div>
</section>

<section class="clients">
  <h2 class="section-title">Our Happy Clients</h2>
  <div class="quote-card" style="left:171px">
    <div class="avatar" role="img" aria-label="Portrait photo of a senior woman client" style="background:linear-gradient(135deg,#e9e4e0,#c8b4aa)"></div>
    <blockquote>Donec dictum lectus non odio Cras a ante vitae enim iaculis aliquam Mauris nunc quam venenatis nec euismod sit amet egestas placerat est</blockquote>
    <cite>By Author Name</cite>
  </div>
  <div class="quote-card" style="left:620px">
    <div class="avatar" role="img" aria-label="Portrait photo of a smiling woman client" style="background:linear-gradient(135deg,#e8c07a,#9c6a4c)"></div>
    <blockquote>Donec dictum lectus non odio Cras a ante vitae enim iaculis aliquam Mauris nunc quam venenatis nec euismod sit amet egestas placerat est</blockquote>
    <cite>By Author Name</cite>
  </div>
</section>

<footer class="site-footer">
  <div class="footer-brand">Go Elderwell<br>Solutions</div>
  <div class="footer-col" style="left:437px">
    <h4>ABOUT US</h4>
    <ul><li>Home</li><li>About Us</li><li>Our Plans</li><li>Get a Free Quote</li></ul>
  </div>
  <div class="footer-col" style="left:635px">
    <h4>RESOURCES</h4>
    <ul><li>Testimonials</li><li>Blogs</li><li>Why Choose Us</li><li>Contact Us</li></ul>
  </div>
  <div class="footer-col" style="left:845px">
    <h4>CONTACT US</h4>
    <ul><li>412 Grand Avenue Suite 210</li><li>Des Moines, IA 50309</li><li>1-800-555-0142</li><li>info@elderwellco.com</li></ul>
    <div class="social"><i></i><i></i><i></i><i></i></div>
  </div>
  <div class="disclaimer">
    <p>This website and its contents are for informational purposes only. Nothing on the website should ever be used as a substitute for professional medical advice. You should always consult with your medical provider regarding diagnosis or treatment for a health condition, including decisions about the correct medication for your condition, as well as prior to undertaking any specific exercise or dietary routine.</p>
    <p>Go Elderwell Solutions is operated by Go Elderwell Solutions, Inc., a licensed health insurance agency certified to sell Elderwell products.</p>
    <p>The purpose of this communication is the solicitation of insurance. Contact will be made by an insurance agent/producer or insurance company.</p>
    <p>Elderwell Supplement insurance plans are not connected with or endorsed by the U.S. government or the federal Elderwell program.</p>
  </div>
  <div class="footer-rule"></div>
  <div class="copyright">© 2017 Company Name. All right reserved. Term of Use</div>
</footer>

</div>
</body>
</html>
```